Web Design Project for an operational risk management consulting company

Website is for a consulting company specialising in operational risk management. Our specialist areas include crisis and emergency management, community engagement, safety and security. We work internationally, generally in high hazard environments. We are a highly ethical and professional company which prides itself on delivering a strong level of customer service.

As a company we recognise that the key to keeping people safe is ensuring that they work in an ethical and sustainable manner. Therefore we are as much about soft skills as we are about hard skills. We would like our website and supporting images to reflect this.
We have worked throughout Africa and the Middle east, as well as Asia pacific. An international flavour to the website would also be great.
Background images on www.corvellpartnersglobal.example are a good example of what we are thinking of, though very open to fresh ideas.

Target Market(s)

Our customers are generally medium to large organisations who work internationally. We would like to also support more not for profits and non government organisations who work in hazardous environments

Industry/Entity Type

It Company

Number of Pages Required

5+ page

Font styles to use
Sans Serif

Requirements
Must have
• Easy to edit by non IT people
• Section for blogs/news updates
• Pages should include:
• (A) home page
• (B) about us
• (C) services
• (D) contact
• (E) insights
Nice to have
• An international and professional theme. Some gritty images that symbolise the risks associated with working in unstable environments, as well as some human ones and that of the environment
Should not have
• Cartoonish or generic images
• Not focus on traditional physical security aspects

```html
<!DOCTYPE html>
<html lang="en">
<head>
<meta charset="utf-8">
<title>Halvern Risk – Operational Risk Management</title>
<link href="https://fonts.googleapis.com/css2?family=Open+Sans:wght@300;400;600;700&display=swap" rel="stylesheet">
<style>
:root{
  --brand:#1d6fb4;
  --brand-dark:#0d4d86;
  --band-1:#0b4f8a;
  --band-2:#1471b8;
  --ink:#333;
  --muted:#777;
  --white:#fff;
  --footer:#2e2e2e;
  --footer-dark:#222;
  --news-bg:#f2f2f2;
}
*{box-sizing:border-box;margin:0;padding:0}
html,body{width:678px;height:1200px;overflow:hidden}
body{font-family:"Open Sans",Arial,sans-serif;color:var(--ink);background:var(--white);position:relative}

.site-header{position:absolute;top:0;left:0;width:678px;height:70px;background:var(--white);display:flex;align-items:center;justify-content:space-between;padding:0 26px 0 20px}
.brand{display:flex;align-items:center;gap:8px}
.brand-mark{width:34px;height:34px;border-radius:50%;background:var(--brand)}
.brand-name{font-size:13px;font-weight:600;color:var(--brand)}
.main-nav{display:flex;gap:30px}
.main-nav a{font-size:8px;letter-spacing:1px;color:#8a8a8a;text-decoration:none;text-transform:uppercase}
.main-nav a.active{color:var(--brand);border-bottom:1px solid var(--brand);padding-bottom:3px}

.hero{position:absolute;top:70px;left:0;width:678px;height:302px;background:linear-gradient(90deg,#4a4d52 0%,#6b6f74 45%,#b9bcbf 75%,#d8d9da 100%)}
.hero-copy{position:absolute;left:42px;top:152px;color:var(--white)}
.hero-title{font-size:22px;font-weight:300;margin-bottom:8px}
.hero-sub{font-size:15px;font-weight:300;margin-bottom:16px}
.btn-outline{display:inline-block;border:1px solid var(--white);color:var(--white);font-size:11px;padding:6px 16px;border-radius:2px}

.welcome{position:absolute;top:372px;left:0;width:678px;height:125px;text-align:center;padding-top:28px}
.welcome h1{font-size:23px;font-weight:300;color:#444}
.welcome h1 span{color:var(--brand)}
.welcome p{width:460px;margin:16px auto 0;font-size:6px;line-height:10px;color:var(--muted)}

.services{position:absolute;top:497px;left:0;width:678px;height:215px;background:linear-gradient(90deg,var(--band-1),var(--band-2) 60%,var(--band-1))}
.services-visual{position:absolute;left:30px;top:20px;width:200px;height:195px;background:radial-gradient(circle at 55% 60%,#d9c2b0 0%,#9bb7d3 35%,rgba(20,90,160,0) 70%)}
.service{position:absolute;top:38px;width:120px;text-align:center;color:var(--white)}
.service-icon{width:66px;height:66px;margin:0 auto 12px;border-radius:50%;border:2px solid rgba(255,255,255,.6);background:rgba(255,255,255,.12);display:flex;align-items:center;justify-content:center}
.service-icon svg{width:40px;height:40px}
.service h3{font-size:10.5px;font-weight:400;line-height:13px;margin-bottom:6px}
.service p{font-size:6px;line-height:9px;color:#bcd7ef}
.s1{left:230px}.s2{left:370px}.s3{left:512px}

.news{position:absolute;top:712px;left:0;width:678px;height:278px;background:var(--news-bg)}
.news h2{text-align:center;font-size:21px;font-weight:300;color:#444;margin-top:28px}
.news h2::after{content:"";display:block;width:30px;height:2px;background:var(--brand);margin:5px auto 0}
.news-grid{position:absolute;top:62px;left:44px;display:flex;gap:12px}
.news-card{width:138px}
.news-thumb{height:96px;border-radius:2px}
.t1{background:linear-gradient(135deg,#dfe6ee,#9fb3c7)}
.t2{background:linear-gradient(135deg,#6d7f93,#c8ccd1)}
.t3{background:linear-gradient(135deg,#d7dde3,#8a96a3)}
.t4{background:linear-gradient(180deg,#a9c3df,#7a9a52)}
.news-card h4{font-size:10px;font-weight:400;color:#1d4f86;margin:10px 0 5px}
.news-card p{font-size:6px;line-height:9px;color:var(--muted)}
.news-card a{display:block;margin-top:10px;font-size:6.5px;font-weight:700;color:var(--brand-dark);text-decoration:none}

.site-footer{position:absolute;top:990px;left:0;width:678px;height:210px;background:var(--footer)}
.contact-row{position:absolute;top:28px;left:0;width:678px;display:flex;justify-content:space-around;padding:0 60px}
.contact-item{width:140px;text-align:center}
.contact-icon{width:30px;height:30px;border-radius:50%;background:#444;margin:0 auto 10px;display:flex;align-items:center;justify-content:center}
.contact-icon svg{width:14px;height:14px}
.contact-item span{font-size:6.5px;color:#8e8e8e}
.footer-base{position:absolute;bottom:0;left:0;width:678px;height:92px;background:var(--footer-dark);text-align:center;padding-top:24px}
.social{display:flex;justify-content:center;gap:6px}
.social span{width:20px;height:20px;border-radius:2px;background:#444}
.social span.on{background:var(--brand)}
.copyright{margin-top:12px;font-size:7px;color:#888}
.copyright b{color:var(--brand);font-weight:400}
</style>
</head>
<body>

<header class="site-header">
  <div class="brand"><span class="brand-mark"></span><span class="brand-name">Halvern Risk</span></div>
  <nav class="main-nav">
    <a class="active" href="#">Home</a><a href="#">About Us</a><a href="#">Services</a><a href="#">Insights</a><a href="#">Contact</a>
  </nav>
</header>

<section class="hero" role="img" aria-label="Photograph of a team meeting around a white table, seen from above">
  <div class="hero-copy">
    <div class="hero-title">Operational Risk Management</div>
    <div class="hero-sub">Ethical and Sustainable Manner</div>
    <span class="btn-outline">Know More</span>
  </div>
</section>

<section class="welcome">
  <h1>Welcome to <span>HALVERN RISK</span></h1>
  <p>Lorem Ipsum is simply dummy text of the printing and typesetting industry. Lorem Ipsum has been the industry's standard dummy text ever since the 1500s, when an unknown printer took a galley of type and scrambled it to make a type specimen book.</p>
</section>

<section class="services">
  <div class="services-visual" role="img" aria-label="Photograph of a hand touching a glowing circular button"></div>
  <div class="service s1">
    <div class="service-icon"><svg viewBox="0 0 40 40" fill="none" stroke="#fff" stroke-width="3"><circle cx="20" cy="20" r="14"/><circle cx="20" cy="20" r="6"/><path d="M10 10l6 6M30 10l-6 6M10 30l6-6M30 30l-6-6"/></svg></div>
    <h3>Crisis &amp; Emergency Management</h3>
    <p>Lorem Ipsum is simply dummy text of the printing and typesetting industry.</p>
  </div>
  <div class="service s2">
    <div class="service-icon"><svg viewBox="0 0 40 40"><circle cx="20" cy="20" r="15" fill="none" stroke="#fff" stroke-width="2"/><path fill="#fff" d="M20 9l3.2 7 7.6.7-5.8 5 1.8 7.4L20 25.3l-6.6 3.8 1.8-7.4-5.8-5 7.6-.7z"/></svg></div>
    <h3>Community Engagement</h3>
    <p>Lorem Ipsum is simply dummy text of the printing and typesetting industry.</p>
  </div>
  <div class="service s3">
    <div class="service-icon"><svg viewBox="0 0 40 40"><path fill="#fff" d="M20 5l12 5v9c0 8-5 13-12 16C13 32 8 27 8 19v-9z"/><path fill="#1471b8" d="M20 9v22c-5-2.5-8-6.5-8-12v-6.5z"/></svg></div>
    <h3>Safety and Security</h3>
    <p>Lorem Ipsum is simply dummy text of the printing and typesetting industry.</p>
  </div>
</section>

<section class="news">
  <h2>Latest News</h2>
  <div class="news-grid">
    <article class="news-card"><div class="news-thumb t1" role="img" aria-label="Photograph of a businessman drawing a network diagram"></div><h4>Lorem Ipsum is a dummy</h4><p>Lorem Ipsum is simply dummy text of the printing and typesetting industry.</p><a href="#">KNOW MORE &gt;&gt;</a></article>
    <article class="news-card"><div class="news-thumb t2" role="img" aria-label="Photograph of a business meeting at a table"></div><h4>Lorem Ipsum is a dummy</h4><p>Lorem Ipsum is simply dummy text of the printing and typesetting industry.</p><a href="#">KNOW MORE &gt;&gt;</a></article>
    <article class="news-card"><div class="news-thumb t3" role="img" aria-label="Photograph of colleagues working together in an office"></div><h4>Lorem Ipsum is a dummy</h4><p>Lorem Ipsum is simply dummy text of the printing and typesetting industry.</p><a href="#">KNOW MORE &gt;&gt;</a></article>
    <article class="news-card"><div class="news-thumb t4" role="img" aria-label="Photograph of hands holding a young plant in soil"></div><h4>Lorem Ipsum is a dummy</h4><p>Lorem Ipsum is simply dummy text of the printing and typesetting industry.</p><a href="#">KNOW MORE &gt;&gt;</a></article>
  </div>
</section>

<footer class="site-footer">
  <div class="contact-row">
    <div class="contact-item"><div class="contact-icon"><svg viewBox="0 0 14 14"><path fill="#999" d="M7 1a4 4 0 0 0-4 4c0 3 4 8 4 8s4-5 4-8a4 4 0 0 0-4-4zm0 5.5A1.5 1.5 0 1 1 7 3.5a1.5 1.5 0 0 1 0 3z"/></svg></div><span>214 Harbour Lane, Westgate</span></div>
    <div class="contact-item"><div class="contact-icon"><svg viewBox="0 0 14 14"><path fill="#999" d="M3 1h2.5l1 3-1.5 1a7 7 0 0 0 4 4l1-1.5 3 1V11a2 2 0 0 1-2 2A10 10 0 0 1 1 3a2 2 0 0 1 2-2z"/></svg></div><span>+1 555 014 2290</span></div>
    <div class="contact-item"><div class="contact-icon"><svg viewBox="0 0 14 14" fill="none" stroke="#999" stroke-width="1.4"><rect x="1.5" y="3" width="11" height="8"/><path d="M1.5 3l5.5 4.5L12.5 3"/></svg></div><span>hello@halvernrisk.example</span></div>
  </div>
  <div class="footer-base">
    <div class="social"><span class="on"></span><span></span><span></span><span></span><span></span></div>
    <p class="copyright">© <b>Halvern Risk</b> 2015. All Rights Reserved.</p>
  </div>
</footer>

</body>
</html>
```